Real Estate Investment Company

Design Powerpoint slides are consistent with our logo, colors, and typeface. These Powerpoint slides will be used in all aspects of the business from live presentations to presentation decks available on a website or via email. Need to have different slide types created that allow for different types of slides such as cover pages, text heavy pages, image and chart heavy pages, multiple column pages, and mixed content pages.
Updates

Reason: to give additional time to get the design correct. I plan on making a selection in the next day or 2

Target Market(s)

Real Estate Investors

Industry/Entity Type

Investment

Other font styles liked:
• Consistent with logo

Requirements
Must have
• Our colors
• Our logo where possible
• Different slide designs of the same theme to allow for different types of slides such as cover pages, text heavy, picture heavy, and mixed content.
• Slides in both portrait and landscape orientation
Nice to have

```html
<!DOCTYPE html>
<html lang="en">
<head>
<meta charset="utf-8">
<title>Halvard Property Group – Slide Theme</title>
<link rel="stylesheet" href="https://fonts.googleapis.com/css2?family=Cinzel:wght@400;600&family=Crimson+Text:wght@400;600;700&display=swap">
<style>
:root{
  --page:#c6c9e5;
  --navy:#1f2c7a;
  --blue:#2a44a3;
  --blue-mid:#3552b4;
  --cyan:#1f9be6;
  --ink:#2a2a35;
  --muted:#5a5a68;
  --pale:#e6ebf4;
  --grey:#d9dbe3;
  --white:#ffffff;
}
*{box-sizing:border-box;margin:0;padding:0}
html,body{width:1200px;height:862px;overflow:hidden;background:var(--page)}
body{position:relative;font-family:"Crimson Text",Georgia,serif;color:var(--ink)}
.slide{position:absolute;width:387px;height:274px;background:var(--white);overflow:hidden}
.c1{left:10px}.c2{left:406px}.c3{left:803px}
.r1{top:10px}.r2{top:294px}.r3{top:578px}
.abs{position:absolute}
.body-text{font-size:6.3px;line-height:1.35;color:var(--ink);text-align:justify}
.body-text p+p{margin-top:6px}
.heading-rule{position:absolute;left:0;width:100%;text-align:center;font-family:"Cinzel",serif;font-size:11px;letter-spacing:3px;color:var(--ink)}
.small-head{font-size:7px;font-weight:600;color:var(--ink)}
.slide-footer{position:absolute;left:0;bottom:0;width:100%;height:14px;background:var(--navy);color:var(--white);font-size:5.6px;display:flex;align-items:center;padding-left:8px;letter-spacing:.2px}
.slide-footer .co{font-family:"Cinzel",serif;font-size:5.8px;margin-right:4px}
.slide-footer .num{position:absolute;right:6px;top:0;height:14px;display:flex;align-items:center;gap:3px;font-size:5.6px}
.slide-footer .num b{font-size:9px;font-weight:400;font-family:"Cinzel",serif}
.brand{position:absolute;font-family:"Cinzel",serif;color:var(--navy);text-align:center}
.brand .name{font-size:13.5px;letter-spacing:.4px;line-height:1}
.brand .sub{font-size:6.5px;letter-spacing:4.5px;margin-top:2px;border-top:1px solid var(--navy);display:inline-block;padding-top:1px}
.band{position:absolute;left:0;top:75px;width:100%;height:96px;background:linear-gradient(90deg,var(--blue) 0%,var(--blue-mid) 100%)}
.cover-photo{position:absolute;left:268px;top:82px;width:104px;height:82px;background:linear-gradient(180deg,#a9a6d8 0%,#4e5a8e 60%,#2f3556 100%)}
.title{position:absolute;left:21px;top:96px;font-family:"Cinzel",serif;font-size:17.5px;color:var(--white);letter-spacing:.5px}
.subtitle{position:absolute;left:21px;top:128px;width:240px;font-size:6.8px;line-height:1.3;color:var(--white)}
.contact{position:absolute;left:0;top:171px;width:145px;height:85px;background:var(--blue);color:var(--white);font-size:7px;padding:10px 0 0 10px}
.contact li{list-style:none;display:flex;align-items:center;gap:6px;height:22px}
.contact svg{width:9px;height:9px;flex:none}
.presented{position:absolute;font-size:7px;line-height:1.2;color:var(--navy)}
.presented strong{font-weight:700}
.base-strip{position:absolute;left:0;bottom:0;width:100%;height:8px;background:var(--navy)}
.axis{font-size:4px;fill:var(--muted)}
.circle-photo{position:absolute;width:42px;height:42px;border-radius:50%;border:2px solid var(--grey)}
.item-head{font-size:6.8px;font-weight:600}
.item-text{font-size:6.3px;line-height:1.3;margin-top:4px}
</style>
</head>
<body>

<section class="slide c1 r1" aria-label="Cover slide">
  <div class="brand" style="left:38px;top:28px"><div class="name">HALVARD PROPERTY</div><div class="sub">GROUP</div></div>
  <div class="band"></div>
  <div class="cover-photo" role="img" aria-label="Photo of a two-storey family house at dusk"></div>
  <div class="title">PRESENTATION TITLE</div>
  <div class="subtitle">Lorem ipsum dolor sit amet, consectetur adipiscing elit.<br>Vestibulum dolor elit, mattis non quam sed, sodales vestibulum justo.</div>
  <ul class="contact">
    <li><svg viewBox="0 0 10 10"><path d="M2 1h2l1 2-1 1a6 6 0 0 0 2 2l1-1 2 1v2c-4 0-7-3-7-7z" fill="#fff"/></svg>+1 555-010-2468</li>
    <li><svg viewBox="0 0 10 10"><rect x="1" y="2" width="8" height="6" fill="#fff"/><path d="M1 2l4 3 4-3" stroke="var(--blue)" fill="none"/></svg>info@halvardproperty.com</li>
    <li><svg viewBox="0 0 10 10"><circle cx="5" cy="5" r="4" fill="none" stroke="#fff"/><path d="M1 5h8M5 1c2 2 2 6 0 8M5 1c-2 2-2 6 0 8" stroke="#fff" fill="none" stroke-width=".7"/></svg>www.halvardproperty.com</li>
  </ul>
  <svg class="abs" style="left:145px;top:171px" width="45" height="85"><polygon points="0,0 45,29 45,85 0,85" fill="var(--grey)"/><polygon points="0,0 45,29 0,29" fill="#eceef3"/></svg>
  <div class="presented" style="left:198px;top:202px">Presented to<br><strong>Company/Client Name</strong><br>31 Jul 2016</div>
  <div class="presented" style="left:305px;top:230px">Presented by<br><strong>Marcus Delaney</strong><br>President</div>
  <div class="base-strip"></div>
</section>

<section class="slide c2 r1" aria-label="About us slide">
  <svg class="abs" style="left:0;top:0" width="195" height="260">
    <defs><linearGradient id="dusk2" x1="0" y1="0" x2="0" y2="1"><stop offset="0" stop-color="#b7b3e0"/><stop offset=".45" stop-color="#d9b9c9"/><stop offset=".7" stop-color="#4d5572"/><stop offset="1" stop-color="#8c96aa"/></linearGradient></defs>
    <polygon role="img" aria-label="Photo of a suburban house with double garage at sunset" points="22,126 158,28 158,266 22,266" fill="url(#dusk2)"/>
  </svg>
  <div class="heading-rule" style="left:100px;width:287px;top:24px">— ABOUT US —</div>
  <div class="abs body-text" style="left:200px;top:50px;width:170px">
    <p>Lorem ipsum dolor sit amet, consectetur adipiscing elit. Vestibulum dolor elit, mattis non quam sed, sodales vestibulum justo. Cras sed accumsan mi, in auctor nisi. Aenean mattis justo molestie, hendrerit velit eget, auctor est.</p>
    <p>Suspendisse mauris mi, pretium eu rhoncus nec, gravida ut lectus. Aliquam faucibus lorem ut rutrum tempor. Vivamus vulputate tempus velit, sed dictum enim fermentum non. In eleifend dui nunc, vel fringilla augue porttitor ac. Ut hendrerit erat et turpis dignissim ullamcorper. Suspendisse potenti.</p>
    <p>Nunc auctor lacus in elit vehicula, in facilisis arcu pretium. Suspendisse ut odio sit amet diam rhoncus pellentesque. Ut egestas ullamcorper massa, quis suscipit urna elementum quis. Interdum et malesuada fames ac ante ipsum primis in faucibus.</p>
    <p>Etiam risus lorem, scelerisque accumsan nulla sit amet, tincidunt congue purus. Nunc ipsum dolor, fermentum sit amet lorem eget, volutpat molestie nisi.</p>
  </div>
  <footer class="slide-footer"><span class="co">HALVARD PROPERTY GROUP</span>© 2016. All rights reserved.<span class="num">Slide <b>02</b></span></footer>
</section>

<section class="slide c3 r1" aria-label="Text slide">
  <div class="heading-rule" style="top:17px">— ALL TEXTS —</div>
  <ul class="abs body-text" style="left:20px;top:42px;width:350px;list-style:none">
    <li>• Lorem ipsum dolor sit amet, consectetur adipiscing elit. Vestibulum dolor elit, mattis non quam sed, sodales vestibulum justo. Cras sed accumsan mi, in auctor nisi. Aenean mattis justo molestie, hendrerit velit eget, auctor est. Suspendisse mauris mi, pretium eu rhoncus nec, gravida ut lectus. Aliquam faucibus lorem ut rutrum tempor. Vivamus vulputate tempus velit, sed dictum enim fermentum non. In eleifend dui nunc, vel fringilla augue porttitor ac. Ut hendrerit erat et turpis dignissim ullamcorper.</li>
    <li style="margin-top:8px">• Suspendisse potenti. Nunc auctor lacus in elit vehicula, in facilisis arcu pretium. Suspendisse ut odio sit amet diam rhoncus pellentesque. Ut egestas ullamcorper massa, quis suscipit urna elementum quis. Interdum et malesuada fames ac ante ipsum primis in faucibus.</li>
    <li style="margin-top:8px">• Etiam risus lorem, scelerisque accumsan nulla sit amet, tincidunt congue purus. Nunc ipsum dolor, fermentum sit amet lorem eget, volutpat molestie nisi. Quisque venenatis, lectus ut vehicula sagittis, nisi mauris faucibus libero, ac egestas arcu diam et odio. Sed id pulvinar dui. Nulla cursus, felis et elementum ullamcorper, nunc tellus egestas justo, pretium egestas justo lacus eu lectus. Sed quis sagittis tellus.</li>
    <li style="margin-top:8px">• Mauris iaculis purus metus, at dignissim turpis venenatis eget. Aenean posuere mi nisi, nec posuere velit dignissim at. Nunc non ligula sit amet erat blandit interdum a sed nibh. Integer sit amet velit vehicula, rhoncus lorem ac, congue lorem. Pellentesque ultricies velit a est ultrices, in venenatis sem luctus.</li>
    <li style="margin-top:8px">• Integer vulputate mollis faucibus. Phasellus metus leo, venenatis non quam non, commodo lobortis risus. Phasellus egestas viverra urna, quis fermentum leo fringilla ac. Suspendisse a posuere velit. Cras pharetra odio sit amet commodo tristique. Mauris suscipit rutrum mi tempor tempus. Pellentesque pellentesque facilisis neque, at interdum diam tincidunt sed. Vestibulum viverra, nibh non egestas egestas, nisi quam fringilla felis, eget aliquet est enim vitae metus.</li>
  </ul>
  <footer class="slide-footer"><span class="co">HALVARD PROPERTY GROUP</span>© 2016. All rights reserved.<span class="num">Slide <b>03</b></span></footer>
</section>

<section class="slide c1 r2" aria-label="Chart slide">
  <div class="abs" style="left:20px;top:15px;font-size:8px">Lorem Ipsum</div>
  <div class="abs body-text" style="left:20px;top:32px;width:165px">Lorem ipsum dolor sit amet, consectetur adipiscing elit. Vestibulum dolor elit, mattis non quam sed, sodales vestibulum justo. Cras sed accumsan mi, in auctor nisi. Aenean mattis justo molestie, hendrerit velit eget, auctor est. Suspendisse mauris mi, pretium eu rhoncus nec, gravida ut lectus. Aliquam faucibus lorem ut rutrum tempor.</div>
  <svg class="abs" style="left:205px;top:35px" width="175" height="60" viewBox="0 0 175 60">
    <text class="axis" x="2" y="4">30</text><text class="axis" x="2" y="16">20</text><text class="axis" x="2" y="28">10</text>
    <path d="M15 44 C35 30 45 20 60 26 S80 18 95 24 S120 8 140 12 S165 30 172 44Z" fill="#f0c9d6" opacity=".8"/>
    <path d="M15 44 C30 34 40 22 55 22 S75 34 90 30 S110 36 125 34 S160 40 172 44Z" fill="#b7e0c9" opacity=".8"/>
    <path d="M15 44 C30 40 45 30 60 32 S85 20 100 10 S125 30 140 26 S160 36 172 44Z" fill="#6e80c8" opacity=".75"/>
    <g class="axis"><text x="18" y="54">1</text><text x="37" y="54">2</text><text x="56" y="54">3</text><text x="75" y="54">4</text><text x="94" y="54">5</text><text x="113" y="54">6</text><text x="132" y="54">7</text><text x="151" y="54">8</text></g>
  </svg>
  <svg class="abs" style="left:18px;top:120px" width="180" height="130" viewBox="0 0 180 130">
    <g stroke="#e2e3ea" stroke-width=".5"><line x1="12" y1="4" x2="175" y2="4"/><line x1="12" y1="21" x2="175" y2="21"/><line x1="12" y1="38" x2="175" y2="38"/><line x1="12" y1="55" x2="175" y2="55"/><line x1="12" y1="72" x2="175" y2="72"/><line x1="12" y1="89" x2="175" y2="89"/><line x1="12" y1="106" x2="175" y2="106"/></g>
    <g class="axis"><text x="2" y="6">6</text><text x="2" y="23">5</text><text x="2" y="40">4</text><text x="2" y="57">3</text><text x="2" y="74">2</text><text x="2" y="91">1</text><text x="2" y="108">0</text></g>
    <g>
      <rect x="20" y="37" width="7" height="69" fill="var(--cyan)"/><rect x="28" y="65" width="7" height="41" fill="var(--navy)"/><rect x="36" y="69" width="7" height="37" fill="var(--blue)"/>
      <rect x="61" y="65" width="7" height="41" fill="var(--cyan)"/><rect x="69" y="31" width="7" height="75" fill="var(--navy)"/><rect x="77" y="72" width="7" height="34" fill="var(--blue)"/>
      <rect x="102" y="46" width="7" height="60" fill="var(--cyan)"/><rect x="110" y="82" width="7" height="24" fill="var(--navy)"/><rect x="118" y="63" width="7" height="43" fill="var(--blue)"/>
      <rect x="143" y="29" width="7" height="77" fill="var(--cyan)"/><rect x="151" y="75" width="7" height="31" fill="var(--navy)"/><rect x="159" y="22" width="7" height="84" fill="var(--blue)"/>
    </g>
    <g class="axis"><text x="22" y="113">Category 1</text><text x="63" y="113">Category 2</text><text x="104" y="113">Category 3</text><text x="145" y="113">Category 4</text></g>
    <g class="axis"><rect x="38" y="119" width="4" height="4" fill="var(--cyan)"/><text x="45" y="123">Label 1</text><rect x="80" y="119" width="4" height="4" fill="var(--navy)"/><text x="87" y="123">Label 2</text><rect x="122" y="119" width="4" height="4" fill="var(--blue)"/><text x="129" y="123">Label 3</text></g>
  </svg>
  <div class="abs" style="left:212px;top:123px;font-size:7.5px">Etiam risus lorem</div>
  <div class="abs body-text" style="left:212px;top:138px;width:165px">Etiam risus lorem, scelerisque accumsan nulla sit amet, tincidunt congue purus. Nunc ipsum dolor, fermentum sit amet lorem eget, volutpat molestie nisi. Quisque venenatis, lectus ut vehicula sagittis, nisi mauris faucibus libero, ac egestas arcu diam et odio. Sed id pulvinar dui. Nulla cursus, felis et elementum ullamcorper, nunc tellus egestas justo, pretium egestas justo lacus eu lectus. Sed quis sagittis tellus. Mauris iaculis purus metus, at dignissim turpis venenatis eget.</div>
  <footer class="slide-footer"><span class="co">HALVARD PROPERTY GROUP</span>© 2016. All rights reserved.<span class="num">Slide <b>04</b></span></footer>
</section>

<section class="slide c2 r2" aria-label="Two column item slide">
  <div class="heading-rule" style="top:18px">— LOREM IPSUM —</div>
  <div class="circle-photo" role="img" aria-label="Photo of an apartment tower" style="left:22px;top:53px;background:linear-gradient(160deg,#7fb2c8,#c9b88c 60%,#6a6a5a)"></div>
  <div class="abs" style="left:82px;top:62px;width:100px"><div class="item-head">Lorem Ipsum</div><div class="item-text">Lorem ipsum dolor sit amet, consectetur adipiscing elit.</div></div>
  <div class="circle-photo" role="img" aria-label="Photo of a modern interior" style="left:206px;top:53px;background:linear-gradient(160deg,#f2f2f2,#8a8a8a 60%,#3a2f28)"></div>
  <div class="abs" style="left:266px;top:62px;width:105px"><div class="item-head">Vestibulum dolor elit</div><div class="item-text">Mattis non quam sed, sodales vestibulum justo.</div></div>
  <div class="circle-photo" role="img" aria-label="Photo of a Victorian townhouse" style="left:22px;top:118px;background:linear-gradient(160deg,#9cc8cf,#f2eee6 55%,#c98a78)"></div>
  <div class="abs" style="left:82px;top:127px;width:100px"><div class="item-head">Vestibulum dolor elit</div><div class="item-text">Mattis non quam sed, sodales vestibulum justo.</div></div>
  <div class="circle-photo" role="img" aria-label="Photo of a warm living room" style="left:206px;top:118px;background:linear-gradient(160deg,#f3e7d2,#c99a64 55%,#6b4a30)"></div>
  <div class="abs" style="left:266px;top:127px;width:105px"><div class="item-head">Cras sed accumsan</div><div class="item-text">Aenean mattis justo molestie, hendrerit velit eget, auctor est.</div></div>
  <div class="circle-photo" role="img" aria-label="Photo of a furnished bedroom" style="left:22px;top:183px;background:linear-gradient(160deg,#e8c98a,#a5713d 55%,#4a3220)"></div>
  <div class="abs" style="left:82px;top:192px;width:100px"><div class="item-head">Cras sed accumsan</div><div class="item-text">Aenean mattis justo molestie, hendrerit velit eget, auctor est.</div></div>
  <div class="circle-photo" role="img" aria-label="Photo of a decorative wall detail" style="left:206px;top:183px;background:linear-gradient(160deg,#f6f3ee,#d8c7a6 60%,#9d8a68)"></div>
  <div class="abs" style="left:266px;top:192px;width:105px"><div class="item-head">Lorem Ipsum</div><div class="item-text">Lorem ipsum dolor sit amet, consectetur adipiscing elit.</div></div>
  <footer class="slide-footer"><span class="co">HALVARD PROPERTY GROUP</span>© 2016. All rights reserved.<span class="num">Slide <b>05</b></span></footer>
</section>

<section class="slide c3 r2" aria-label="Picture slide">
  <svg class="abs" style="left:0;top:0" width="387" height="260">
    <defs><linearGradient id="town" x1="0" y1="0" x2="1" y2="1"><stop offset="0" stop-color="#6fb3bd"/><stop offset=".4" stop-color="#eeebe4"/><stop offset=".7" stop-color="#d8947f"/><stop offset="1" stop-color="#8a8f86"/></linearGradient></defs>
    <polygon role="img" aria-label="Photo of a row of Victorian townhouses" points="47,0 318,0 318,110 183,246 47,110" fill="url(#town)"/>
  </svg>
  <div class="abs body-text" style="left:19px;top:120px;width:160px;text-align:left">Lorem<br>ipsum dolor sit<br>amet, consectetur<br>adipiscing elit.<br>Vestibulum dolor elit,<br>mattis non quam sed, sodales<br>vestibulum justo. Cras sed<br>accumsan mi, in auctor nisi. Aenean<br>mattis justo molestie, hendrerit velit eget,<br>auctor est. Suspendisse mauris mi, pretium eu<br>rhoncus nec, gravida ut lectus. Aliquam faucibus<br>lorem ut rutrum tempor. Vivamus vulputate<br>tempus velit, sed dictum enim fermentum non. In<br>eleifend dui nunc, vel fringilla augue porttitor ac.</div>
  <div class="abs body-text" style="left:208px;top:120px;width:160px;text-align:right">Ut<br>hendrerit erat<br>et turpis dignissim<br>ullamcorper.<br>Suspendisse potenti. Nunc<br>auctor lacus in elit vehicula, in<br>facilisis arcu pretium. Suspendisse<br>ut odio sit amet diam rhoncus<br>pellentesque. Ut egestas ullamcorper<br>massa, quis suscipit urna elementum quis.<br>Interdum et malesuada fames ac ante ipsum primis<br>in faucibus. Quisque venenatis, lectus ut vehicula<br>sagittis, nisi mauris faucibus libero, ac egestas arcu<br>diam et odio. Sed id pulvinar dui.</div>
  <footer class="slide-footer"><span class="co">HALVARD PROPERTY GROUP</span>© 2016. All rights reserved.<span class="num">Slide <b>06</b></span></footer>
</section>

<section class="slide c1 r3" aria-label="Mixed content slide">
  <div class="abs" role="img" aria-label="Desktop monitor showing an area chart" style="left:27px;top:13px;width:90px;height:57px;background:linear-gradient(180deg,#2c2f3a,#5c6070)"></div>
  <div class="abs small-head" style="left:140px;top:13px">Lorem ipsum dolor sit amet</div>
  <div class="abs body-text" style="left:140px;top:29px;width:232px">Consectetur adipiscing elit. Vestibulum dolor elit, mattis non quam sed, sodales vestibulum justo. Cras sed accumsan mi, in auctor nisi. Aenean mattis justo molestie, hendrerit velit eget, auctor est. Suspendisse mauris mi, pretium eu rhoncus nec, gravida ut lectus. Aliquam faucibus lorem ut rutrum tempor.</div>
  <div class="abs" style="left:0;top:86px;width:387px;height:86px;background:var(--pale)"></div>
  <div class="abs small-head" style="left:25px;top:97px">Etiam risus lorem</div>
  <div class="abs body-text" style="left:25px;top:112px;width:230px">Etiam risus lorem, scelerisque accumsan nulla sit amet, tincidunt congue purus. Nunc ipsum dolor, fermentum sit amet lorem eget, volutpat molestie nisi. Quisque venenatis, lectus ut vehicula sagittis, nisi mauris faucibus libero, ac egestas arcu diam et odio. Sed id pulvinar dui. Nulla cursus, felis et elementum ullamcorper, nunc tellus egestas justo, pretium egestas justo lacus eu lectus. Sed quis sagittis tellus.</div>
  <div class="abs" role="img" aria-label="Laptop showing a bar chart" style="left:268px;top:100px;width:100px;height:62px;background:linear-gradient(180deg,#2c2f3a,#5c6070)"></div>
  <div class="abs" role="img" aria-label="Monitor and tablet showing slide layouts" style="left:27px;top:183px;width:100px;height:56px;background:linear-gradient(180deg,#2c2f3a,#5c6070)"></div>
  <div class="abs small-head" style="left:140px;top:185px">Etiam risus lorem</div>
  <div class="abs body-text" style="left:140px;top:200px;width:232px">Scelerisque accumsan nulla sit amet, tincidunt congue purus. Nunc ipsum dolor, fermentum sit amet lorem eget, volutpat molestie nisi. Quisque venenatis, lectus ut vehicula sagittis, nisi mauris faucibus libero, ac egestas arcu diam et odio. Sed id pulvinar dui. Nulla cursus, felis et elementum ullamcorper, nunc tellus egestas justo, pretium egestas justo lacus eu lectus. Sed quis sagittis tellus.</div>
  <footer class="slide-footer"><span class="co">HALVARD PROPERTY GROUP</span>© 2016. All rights reserved.<span class="num">Slide <b>07</b></span></footer>
</section>

<section class="slide c2 r3" aria-label="Photo grid slide">
  <div class="abs" role="img" aria-label="Photo of a tall apartment block against a blue sky" style="left:7px;top:6px;width:131px;height:248px;background:linear-gradient(180deg,#23566a 0%,#3e7a80 35%,#e6e0c3 60%,#8a8a6a 100%)"></div>
  <div class="abs" role="img" aria-label="Photo of a Victorian townhouse facade" style="left:144px;top:6px;width:116px;height:87px;background:linear-gradient(180deg,#78bcc3,#eeebe4 50%,#d09080)"></div>
  <div class="abs" role="img" aria-label="Photo of a family house at dusk" style="left:266px;top:6px;width:115px;height:87px;background:linear-gradient(180deg,#b7b3e0,#d9b9c9 40%,#3e4668 70%,#7c86a0)"></div>
  <div class="abs small-head" style="left:150px;top:114px">Etiam risus lorem</div>
  <div class="abs body-text" style="left:150px;top:130px;width:228px">
    <p>Scelerisque accumsan nulla sit amet, tincidunt congue purus. Nunc ipsum dolor, fermentum sit amet lorem eget, volutpat molestie nisi. Quisque venenatis, lectus ut vehicula sagittis, nisi mauris faucibus libero, ac egestas arcu diam et odio. Sed id pulvinar dui. Nulla cursus, felis et elementum ullamcorper, nunc tellus egestas justo, pretium egestas justo lacus eu lectus. Sed quis sagittis tellus.</p>
    <p>Mauris iaculis purus metus, at dignissim turpis venenatis eget. Aenean posuere mi nisi, nec posuere velit dignissim at. Nunc non ligula sit amet erat blandit interdum a sed nibh. Integer sit amet velit vehicula, rhoncus lorem ac, congue lorem. Pellentesque ultricies velit a est ultrices, in venenatis sem luctus.</p>
  </div>
  <footer class="slide-footer"><span class="co">HALVARD PROPERTY GROUP</span>© 2016. All rights reserved.<span class="num">Slide <b>08</b></span></footer>
</section>

<section class="slide c3 r3" aria-label="Closing slide">
  <div class="brand" style="left:46px;top:28px"><div class="name">HALVARD PROPERTY</div><div class="sub">GROUP</div></div>
  <div class="band"></div>
  <div class="cover-photo" role="img" aria-label="Photo of a two-storey family house at dusk"></div>
  <div class="title" style="left:63px;top:110px;font-size:19px">THANK YOU!</div>
  <ul class="contact">
    <li><svg viewBox="0 0 10 10"><path d="M2 1h2l1 2-1 1a6 6 0 0 0 2 2l1-1 2 1v2c-4 0-7-3-7-7z" fill="#fff"/></svg>+1 555-010-2468</li>
    <li><svg viewBox="0 0 10 10"><rect x="1" y="2" width="8" height="6" fill="#fff"/><path d="M1 2l4 3 4-3" stroke="var(--blue)" fill="none"/></svg>info@halvardproperty.com</li>
    <li><svg viewBox="0 0 10 10"><circle cx="5" cy="5" r="4" fill="none" stroke="#fff"/><path d="M1 5h8M5 1c2 2 2 6 0 8M5 1c-2 2-2 6 0 8" stroke="#fff" fill="none" stroke-width=".7"/></svg>www.halvardproperty.com</li>
  </ul>
  <svg class="abs" style="left:145px;top:171px" width="45" height="85"><polygon points="0,0 45,29 45,85 0,85" fill="var(--grey)"/><polygon points="0,0 45,29 0,29" fill="#eceef3"/></svg>
  <div class="presented" style="left:198px;top:202px">Presented to<br><strong>Company/Client Name</strong><br>31 Jul 2016</div>
  <div class="presented" style="left:305px;top:230px">Presented by<br><strong>Marcus Delaney</strong><br>President</div>
  <div class="base-strip"></div>
</section>

</body>
</html>
```